Homepage für Unternehmensberatung
Zielgruppe
Wir sind eine Unternehmensberatung mit einem klaren Branchenfokus auf Banken / Finanzdienstleister.
Unsere Dienstleistungsprodukte lassen sich grob in folgende Themencluster unterteilen:
1)Strategieentwicklung
o IT-Strategie, IT-Architektur, IT-Bebauungsplan
2) Projektmanagement
o Projektportfoliomgmt., Programmmgmt., Projektmanagement, Projektcontrolling
3) Fachberatung
o Bankfachliche IT- Beratung mit Schwerpunkten Kredit, Wertpapiergeschäft,
Bankenaufsichtsrecht, Liquiditätsmanagement
o Anforderungsmanagement inkl. Aufbau von Bewertungs- und Priorisierungsmethoden
4) Prozessberatung/-optimierung
o Prozessanalyse, Prozessdesign, Prozessdokumentation
o Prozessoptimierung auf Basis etablierter Messmethoden
Unser Firmenname Lindenhofer hat für uns eine Doppelbedeutung:
1. Im Außenverhältnis: Wir verstehen uns als Lindenhofer unserer Kunden
2. Im Innenverhältnis: Wir pflegen einen partnerschaftlichen Umgang mit unseren
Mitarbeitern (Teamarbeit)
Aktuell sind wir ein kleines aber feines Team von erfahrenen und hochmotivierten Kollegen. Unsere Mitarbeiter sind ehemalige Führungskräfte sowie erfahrenen Unternehmensberater.
Aufgabenstellung
Entwurf / Design von 2 Seiten:
1. Seite / Startseite:
Simple und elegante Darstellung der oben genannten 4 Themencluster (z.B. Bild/Piktogramm, Textkasten) sowie einer Navigationsmöglichkeit zu folgenden Detailsichten:
• Unternehmen
• Beratungsangebot (siehe Themencluster)
• Partnerunternehmen
• Kontakt
2. Seite / 2. Ebene:
Entwurf einer Möglichkeit zur Erläuterung/Darstellung von Inhalten der Startseite.
Die Themencluster sollten auf jeder Ebene immer „anklickbar“/ zu sehen sein.
Logo
Das angehängte Logo ist in die Website einzubinden. Stil und Farben sollen übernommen werden bzw. sind Basis für das Design.
Lizenzen
Lizenz für eingesetzte Fotos und Illustrationen soll enthalten / Open-Source sein. Wenn nicht dann bitte zusätzliche Kosten angeben.

```html
<!DOCTYPE html>
<html lang="de">
<head>
<meta charset="utf-8">
<title>Lindenhofer – Unternehmensberatung</title>
<link rel="stylesheet" href="https://fonts.googleapis.com/css2?family=Open+Sans:wght@400;700&family=Roboto+Condensed:wght@700&family=Bebas+Neue&display=swap">
<style>
  :root {
    --brand-blue: #1a7ab3;
    --brand-blue-light: #2a93d3;
    --brand-blue-dark: #1467a0;
    --slate: #5a6166;
    --arrow-grey: #6b7176;
    --city-dark: #15181b;
    --city-mid: #3b3f43;
    --white: #ffffff;
    --muted: #8a8f93;
  }
  * { box-sizing: border-box; margin: 0; padding: 0; }
  html, body { width: 1200px; height: 686px; overflow: hidden; }
  body { position: relative; font-family: "Open Sans", Arial, sans-serif; background: var(--city-dark); }

  .backdrop {
    position: absolute; inset: 0;
    background: linear-gradient(180deg, #4a4d50 0%, #2e3134 35%, #1c1f22 65%, #101214 100%);
  }

  .site { position: absolute; left: 180px; top: 88px; width: 842px; }

  .nav-bar {
    position: absolute; left: 0; top: 30px; width: 842px; height: 47px;
    background: var(--brand-blue);
  }
  .nav-list {
    position: absolute; right: 20px; top: 0; height: 47px;
    display: flex; align-items: center; gap: 28px; list-style: none;
  }
  .nav-list a { color: var(--white); font-weight: 700; font-size: 13px; text-decoration: none; }

  .logo-box {
    position: absolute; left: 15px; top: 0; width: 294px; height: 77px;
    background: var(--white);
    display: flex; align-items: center; gap: 12px; padding-left: 14px;
  }
  .logo-dot { width: 52px; height: 52px; border-radius: 50%; background: var(--brand-blue); }
  .logo-name { color: var(--brand-blue); font-size: 24px; font-weight: 400; font-family: "Open Sans", Arial, sans-serif; }

  .hero {
    position: absolute; left: 0; top: 77px; width: 842px; height: 409px;
    background: linear-gradient(90deg, #9bb6c9 0%, #c9dbe6 35%, #e4ecf1 55%, #8fb3cf 75%, #b9d3e4 100%);
    border-bottom: 5px solid var(--brand-blue);
  }

  .services {
    position: absolute; left: 74px; top: 211px; width: 299px; height: 258px;
    border: 1px solid rgba(255,255,255,0.35);
    background: rgba(30,45,60,0.15);
  }
  .service {
    position: absolute; left: 6px; width: 284px;
    background: linear-gradient(180deg, var(--brand-blue-light), var(--brand-blue-dark));
    display: flex; align-items: center; gap: 16px; padding-left: 10px;
    color: var(--white); font-family: "Roboto Condensed", Arial, sans-serif; font-weight: 700;
    font-size: 16px; line-height: 1.2; text-transform: uppercase;
  }
  .service svg { flex: none; width: 32px; height: 32px; }
  .s1 { top: 8px; height: 43px; }
  .s2 { top: 64px; height: 62px; }
  .s3 { top: 136px; height: 45px; }
  .s4 { top: 189px; height: 62px; }

  .tagline {
    position: absolute; left: 493px; top: 348px; width: 349px; height: 80px;
    background: var(--slate); border-left: 5px solid var(--brand-blue);
    display: flex; align-items: center; padding-left: 18px;
    color: var(--white); font-family: "Bebas Neue", Impact, sans-serif; font-size: 28px; letter-spacing: 0.5px;
  }

  .slider-arrow {
    position: absolute; top: 320px; width: 40px; height: 53px;
    background: var(--arrow-grey); display: flex; align-items: center; justify-content: center;
  }
  .slider-arrow.prev { left: 158px; }
  .slider-arrow.next { left: 1000px; }

  .footer-copy {
    position: absolute; left: 180px; top: 596px;
    color: var(--muted); font-size: 11px;
  }
  .social { position: absolute; left: 880px; top: 591px; display: flex; gap: 6px; list-style: none; }
  .social li { width: 22px; height: 22px; border-radius: 50%; background: #707479; }
</style>
</head>
<body>
  <div class="backdrop" role="img" aria-label="Dunkle Stadtansicht mit Hochhäusern bei bewölktem Himmel"></div>

  <div class="site">
    <header>
      <nav class="nav-bar">
        <ul class="nav-list">
          <li><a href="#">COMPANY</a></li>
          <li><a href="#">CONSULTING SERVICE</a></li>
          <li><a href="#">PARTNER COMPANIES</a></li>
          <li><a href="#">CONTACT</a></li>
        </ul>
      </nav>
      <div class="logo-box">
        <span class="logo-dot"></span>
        <span class="logo-name">Lindenhofer</span>
      </div>
    </header>

    <section class="hero" role="img" aria-label="Foto: lächelnde Beraterin im Nadelstreifen-Blazer vor einem Team im hellen Büro">
    </section>

    <div class="services">
      <a class="service s1">
        <svg viewBox="0 0 32 32" fill="none" stroke="#fff" stroke-width="2.5"><circle cx="16" cy="16" r="13"/><path d="M11 21l3-8 8-3-3 8z" fill="#fff" stroke-width="1"/></svg>
        <span>Strategy Development</span>
      </a>
      <a class="service s2">
        <svg viewBox="0 0 32 32" fill="none" stroke="#fff" stroke-width="3"><path d="M7 14a9 9 0 0 1 16-5"/><path d="M25 18a9 9 0 0 1-16 5"/><path d="M20 6l4 3-4 3" stroke-width="2.5"/><path d="M12 26l-4-3 4-3" stroke-width="2.5"/></svg>
        <span>Process Consulting and<br>Optimization</span>
      </a>
      <a class="service s3">
        <svg viewBox="0 0 32 32" fill="#fff"><rect x="12" y="6" width="8" height="6"/><rect x="3" y="21" width="7" height="6"/><rect x="12.5" y="21" width="7" height="6"/><rect x="22" y="21" width="7" height="6"/><path d="M15 12h2v4h10v5h-2v-3H17v3h-2v-3H7v3H5v-5h10z"/></svg>
        <span>Project Management</span>
      </a>
      <a class="service s4">
        <svg viewBox="0 0 32 32" fill="none" stroke="#fff" stroke-width="2.2"><circle cx="16" cy="12" r="8"/><path d="M12 20v4h8v-4"/><path d="M13 27h6"/></svg>
        <span>Professional Consulting<br>Services</span>
      </a>
    </div>

    <div class="tagline">A beautiful tagline goes here</div>
  </div>

  <a class="slider-arrow prev" aria-label="Zurück">
    <svg width="14" height="22" viewBox="0 0 14 22"><path d="M11 2L3 11l8 9" fill="none" stroke="#b9bdc0" stroke-width="3"/></svg>
  </a>
  <a class="slider-arrow next" aria-label="Weiter">
    <svg width="14" height="22" viewBox="0 0 14 22"><path d="M3 2l8 9-8 9" fill="none" stroke="#b9bdc0" stroke-width="3"/></svg>
  </a>

  <footer>
    <p class="footer-copy">Copyright 2014. All rights reserved.</p>
    <ul class="social" aria-label="Soziale Netzwerke">
      <li></li><li></li><li></li><li></li><li></li>
    </ul>
  </footer>
</body>
</html>
```